CyberSecurity Company Website Design

DO NOT CONTACT US OUTSIDE OF PIXELBAZAAR.COM!

A professional 5 page website design for a cyber security and risk management company. We want to portray a serious and professional approach to online security and risk management for businesses. We want the website to be easy to navigate but with a modern style.

The website design pages my partners have reviewed and wish to emulate (without copying, of course ) are:
wrenforge.com, larkhollow.com and brunel.com, Gavromill.com

The attached Zip file contains a very basic outline of the format we are looking for. We want a nice, modern design that reflects cyber security, securing networks, and risk management for business.

Target Market(s)

Large corporations with CyberSecurity Needs

Number of Pages Required

5+ page

Colors
ec1f27
ffffff
0293ce

Requirements
Must have
• The 5 pages we need designed are;
• Home page, Services, About Us, Careers and Contact.

```html
<!DOCTYPE html>
<html lang="en">
<head>
<meta charset="utf-8">
<title>Veltrano CyberTech</title>
<link href="https://fonts.googleapis.com/css2?family=Lato:ital,wght@0,300;0,400;0,700;1,400;1,700&display=swap" rel="stylesheet">
<style>
:root{
  --red:#ec1f27;
  --red-soft:#e8434a;
  --blue:#0293ce;
  --navy:#141a3a;
  --navy-deep:#0f1430;
  --ink:#333a4a;
  --muted:#6b7080;
  --white:#ffffff;
  --grey-bar:#9a9ca3;
  --line:#e2e4ea;
}
*{box-sizing:border-box;margin:0;padding:0}
html,body{width:1200px;height:3156px;overflow:hidden}
body{font-family:'Lato',sans-serif;color:var(--ink);background:var(--white)}
.site-header{height:140px;display:flex;align-items:center;justify-content:space-between;padding:0 100px 0 104px}
.brand{font-size:58px;font-weight:400;color:var(--red);letter-spacing:1px}
.main-nav{display:flex;align-items:center;gap:38px;font-size:17px;color:#3a3f4d}
.main-nav .active{color:var(--red)}
.social{display:flex;gap:8px;margin-left:4px}
.social span{width:20px;height:20px;background:#2c5a9a;display:block}
.hero{position:relative;height:640px;background:radial-gradient(ellipse at 50% 45%,#4fc3f2 0%,#139be0 40%,#0a5fae 100%)}
.hero .arrow{position:absolute;top:300px;width:40px;height:40px}
.hero .arrow.left{left:30px}.hero .arrow.right{right:30px}
.welcome{height:470px;text-align:center;padding-top:88px}
.section-title{font-size:38px;font-weight:400;color:var(--red)}
.rule{width:60px;height:3px;background:var(--navy);margin:18px auto 28px}
.welcome p{width:540px;margin:0 auto 14px;font-size:14px;line-height:22px;color:var(--muted)}
.btn{display:inline-block;background:var(--red);color:var(--white);font-size:14px;padding:10px 32px;border-radius:3px;margin-top:14px}
.services{height:420px;display:flex;background:var(--navy)}
.services-intro{width:510px;padding:60px 0 0 100px;color:#c9cce0}
.services-intro .section-title{text-align:left}
.services-intro .rule{margin:18px 0 28px;background:var(--white)}
.services-intro p{font-size:14px;line-height:22px;width:300px;margin-bottom:14px}
.services-panel{flex:1;position:relative;background:linear-gradient(135deg,#27304f 0%,#3a4668 50%,#202843 100%);padding:70px 50px 0 60px;display:grid;grid-template-columns:repeat(3,1fr);grid-auto-rows:150px;column-gap:30px}
.service h3{display:flex;align-items:center;gap:10px;font-size:14px;font-weight:700;color:var(--white);margin-bottom:10px}
.service h3 svg{flex:none}
.service p{font-size:11px;line-height:16px;color:#b8bdd2}
.team{height:615px;text-align:center;padding-top:52px}
.team .sub{font-size:28px;font-style:italic;font-weight:700;color:var(--navy);margin-top:8px}
.team .org{font-size:17px;font-weight:700;color:var(--red);margin-top:4px}
.team .rule{margin:14px auto 40px;background:var(--red)}
.members{display:flex;justify-content:center;gap:170px}
.member{width:200px}
.portrait{width:190px;height:190px;border-radius:50%;margin:0 auto 22px;background:radial-gradient(circle at 50% 40%,#b99a86,#6d5b55 70%,#3d3a44);border:4px solid #f1f1f3}
.member h4{font-size:19px;font-weight:400;color:var(--red)}
.member .role{font-size:13px;color:var(--muted);margin-top:4px}
.member .social{justify-content:center;margin-top:10px;gap:6px}
.member .social span{width:16px;height:16px}
.testimonials{height:555px;position:relative;background:radial-gradient(ellipse at 35% 40%,#f0434a,#d5141c 60%,#b90f16);text-align:center;color:var(--white);padding-top:62px}
.testimonials .section-title{color:var(--white)}
.testimonials .sub{font-size:24px;font-style:italic;font-weight:700;color:var(--navy);margin-top:6px}
.testimonials .rule{background:var(--white);margin:14px auto 70px}
.quotes{display:flex;justify-content:center;gap:48px}
.quote{width:300px;position:relative;text-align:left}
.card{background:var(--white);color:var(--muted);font-size:12px;line-height:18px;padding:64px 24px 26px 34px;height:190px;position:relative}
.card::after{content:"";position:absolute;right:40px;bottom:-14px;border:14px solid transparent;border-top-color:var(--white);border-bottom:0}
.avatar{position:absolute;left:30px;top:-36px;width:80px;height:80px;border-radius:50%;background:radial-gradient(circle at 50% 40%,#a88a78,#4a4048 75%);border:4px solid var(--white);z-index:1}
.quote cite{display:block;text-align:right;font-style:normal;font-size:13px;font-weight:700;color:var(--white);margin-top:24px;padding-right:20px}
.testimonials .arrow{position:absolute;top:290px;width:40px;height:40px}
.testimonials .arrow.left{left:30px}.testimonials .arrow.right{right:30px}
.site-footer{height:250px;background:var(--navy-deep);text-align:center;padding-top:46px;color:#c9cce0}
.site-footer .brand{font-size:54px}
.site-footer .office{font-size:14px;font-weight:700;color:var(--white);margin-top:4px}
.site-footer .place{font-size:12px;margin-top:2px}
.site-footer .contact{font-size:12px;margin-top:22px}
.legal{height:66px;background:var(--grey-bar);color:#eceef2;font-size:12px;display:flex;align-items:center;justify-content:center;gap:14px}
</style>
</head>
<body>
<header class="site-header">
  <div class="brand">Veltrano</div>
  <nav class="main-nav">
    <span class="active">Home</span><span>Services</span><span>About Us</span><span>Careers</span><span>Contact</span>
    <div class="social" aria-label="Social links"><span></span><span></span><span></span></div>
  </nav>
</header>

<section class="hero" role="img" aria-label="Hero photo: hands framing the Veltrano name amid glowing padlock icons on a blue network background">
  <svg class="arrow left" viewBox="0 0 40 40"><path d="M25 8 13 20l12 12" stroke="#fff" stroke-width="4" fill="none"/></svg>
  <svg class="arrow right" viewBox="0 0 40 40"><path d="M15 8l12 12-12 12" stroke="#fff" stroke-width="4" fill="none"/></svg>
</section>

<section class="welcome">
  <h2 class="section-title">Welcome to VCT</h2>
  <div class="rule"></div>
  <p>We provide advanced security engineering and cybersecurity architecture solutions for the commercial sector and federal government.</p>
  <p>Our security experts create customized IT solutions that protect organizations, meet compliance requirements and keep critical business systems running safely every day.</p>
  <p>It's all about YOU, our customer, your needs and your safety.</p>
  <span class="btn">Read More</span>
</section>

<section class="services">
  <div class="services-intro">
    <h2 class="section-title">Services at VCT</h2>
    <div class="rule"></div>
    <p>Lorem ipsum dolor sit amet, consectetur adipiscing elit. Quid autem habent admirationis, cum prope accesseris?</p>
    <p>Nam quibus rebus efficiuntur voluptates, eae non sunt in potestate sapientis.</p>
    <span class="btn">Read More</span>
  </div>
  <div class="services-panel" role="img" aria-label="Background photo of a person working at a laptop, overlaid with the service list">
    <div class="service"><h3><svg width="22" height="18"><rect x="1" y="1" width="20" height="13" fill="none" stroke="#fff" stroke-width="2"/><rect x="6" y="15" width="10" height="2" fill="#fff"/></svg>Cyber Security</h3><p>Layered defence for networks and data, built around your business risk.</p></div>
    <div class="service"><h3><svg width="22" height="18"><rect x="1" y="3" width="20" height="13" fill="none" stroke="#fff" stroke-width="2"/><path d="M1 4l10 7 10-7" stroke="#fff" stroke-width="2" fill="none"/></svg>Encrypted Messaging</h3><p>Private channels that keep every message sealed from end to end.</p></div>
    <div class="service"><h3><svg width="22" height="18"><circle cx="11" cy="9" r="8" fill="none" stroke="#fff" stroke-width="2"/><path d="M7 9l3 3 5-6" stroke="#fff" stroke-width="2" fill="none"/></svg>Secure Payment</h3><p>Protected transactions with monitoring that stops fraud early.</p></div>
    <div class="service"><h3><svg width="22" height="18"><rect x="1" y="3" width="20" height="13" fill="none" stroke="#fff" stroke-width="2"/><path d="M11 6v5M11 13v1" stroke="#fff" stroke-width="2"/></svg>E-mail Virus Threat</h3><p>Filtering that catches malicious mail before it reaches staff.</p></div>
    <div class="service"><h3><svg width="22" height="18"><rect x="6" y="1" width="10" height="16" rx="2" fill="none" stroke="#fff" stroke-width="2"/></svg>Mobile Security</h3><p>Device policies and protection for a team that works anywhere.</p></div>
    <div class="service"><h3><svg width="22" height="18"><circle cx="11" cy="9" r="7" fill="none" stroke="#fff" stroke-width="2"/><path d="M8 9c0-3 6-3 6 0v4" stroke="#fff" stroke-width="2" fill="none"/></svg>Finger Print Scanner</h3><p>Biometric access control for rooms, devices and key systems.</p></div>
  </div>
</section>

<section class="team">
  <h2 class="section-title">Amazing Team at Veltrano</h2>
  <div class="sub">Meet our Partners</div>
  <div class="org">Veltrano CyberTech (VCT)</div>
  <div class="rule"></div>
  <div class="members">
    <div class="member"><div class="portrait" role="img" aria-label="Portrait photo of Marcus Lindell"></div><h4>Marcus Lindell</h4><div class="role">CEO</div><div class="social"><span></span><span></span><span></span></div></div>
    <div class="member"><div class="portrait" role="img" aria-label="Portrait photo of Joan Ravel"></div><h4>Joan Ravel</h4><div class="role">VP Business Development</div><div class="social"><span></span><span></span><span></span></div></div>
    <div class="member"><div class="portrait" role="img" aria-label="Portrait photo of Omar Keswick"></div><h4>Omar Keswick</h4><div class="role">CTO</div><div class="social"><span></span><span></span><span></span></div></div>
  </div>
</section>

<section class="testimonials" role="region" aria-label="Testimonials over a red globe background">
  <h2 class="section-title">Awesome People Talk About VCT</h2>
  <div class="sub">Our Customers are Our Heroes!</div>
  <div class="rule"></div>
  <div class="quotes">
    <div class="quote"><div class="avatar" role="img" aria-label="Photo of Peter Hale"></div><div class="card">Since we started working with the team our systems feel safer. Response is quick and every report is clear and easy to follow.</div><cite>Peter Hale</cite></div>
    <div class="quote"><div class="avatar" role="img" aria-label="Photo of Neil Ashford"></div><div class="card">No one takes care of our customer data quite like these experts. They guard it around the clock with care.</div><cite>Neil Ashford</cite></div>
    <div class="quote"><div class="avatar" role="img" aria-label="Photo of Colin Brandt"></div><div class="card">I can sleep at night, and so can my executive team, thanks to all of the work they do and the advice they give.</div><cite>Colin Brandt</cite></div>
  </div>
  <svg class="arrow left" viewBox="0 0 40 40"><path d="M25 8 13 20l12 12" stroke="#fff" stroke-width="4" fill="none"/></svg>
  <svg class="arrow right" viewBox="0 0 40 40"><path d="M15 8l12 12-12 12" stroke="#fff" stroke-width="4" fill="none"/></svg>
</section>

<footer class="site-footer">
  <div class="brand">Veltrano</div>
  <div class="office">Veltrano Corporate Office</div>
  <div class="place">Harbor Square</div>
  <div class="contact">Phone: 212-555-0142 &nbsp; Fax: 212-555-0199 &nbsp; Email: contact@veltrano.example &nbsp; Web: www.veltrano.example</div>
</footer>
<div class="legal"><span>© 2017 Veltrano</span><span>|</span><span>Privacy Policy</span><span>|</span><span>User Agreement</span></div>
</body>
</html>
```